Drug safety monitoring company requires a new corporate website

We are an outsourcing partner to large and small companies within the pharmaceutical industry. Our current website www.orbanquill.co.uk has not been updated in a long time. We want a new web site that is responsive and modern but with a clearly corporate and professional feel. We want a design based on a 12 column grid system (mobile and desktop version). We want to use a new, modern font (not the standard web fonts) - we will purchase as required. Content can be used as is from the current website. Red and white are the corporate colours, so a palate should be developed to match. We do not need as much red as is in the current website. New icons (preferably in svg format) would be great. We can also purchase new images from PhotoVane (or other) as required. We would prefer submissions in Sketch if possible.

Target Market(s)

Pharmaceutical companies

Number of Pages Required

1 page

Font styles to use
Sans Serif

Colors
ec1f27
ffffff

Requirements
Must have
• Design based on 12 column grid system.
Responsive design (i.e. require a mobile and desktop version).
How should the menu look between desktop and mobile?
A coherent colour palete.
Content to come from the existing website: www.orbanquill.co.uk
How should links be styled?
How should headings, sub-headings, paragraphs be styled?
Nice to have
• Custom developed icons (these are along the bottom of the page on the existing website: Medical Information; Pharmacovigilance; Literature Monitoring; Training).
New imagery (the images on the current website are dated).
Submission ideally as Sketch files (but we are okay with photoshop too).
A new, modern, non-standard font.
Not so much red in the design.
If we had buttons on the website, how should they be styled?
If we had a form on the website, how should the fields be styled?

```html
<!DOCTYPE html>
<html lang="en">
<head>
<meta charset="utf-8">
<title>Orban Quill – Pharmacovigilance</title>
<link rel="stylesheet" href="https://fonts.googleapis.com/css2?family=Open+Sans:wght@400;600;700&display=swap">
<style>
:root{
  --red:#ec1f27;
  --red-deep:#e50914;
  --ink:#2b2b2b;
  --text:#3a3a3a;
  --muted:#555c66;
  --white:#ffffff;
  --hero-bg:#e8eef6;
  --soft-bg:#f6f8fb;
  --card-shadow:rgba(40,60,90,0.08);
}
*{box-sizing:border-box;margin:0;padding:0}
html,body{width:1200px;height:2238px;overflow:hidden;background:var(--white)}
body{font-family:"Open Sans",sans-serif;color:var(--text)}
.page{position:relative;width:1200px;height:2238px;overflow:hidden;background:var(--soft-bg)}
.abs{position:absolute}

/* Header */
.site-header{left:0;top:0;width:1200px;height:110px;background:var(--white)}
.brand{left:150px;top:40px;font-size:19px;font-weight:700;letter-spacing:2px;color:var(--red);line-height:1}
.nav a{position:absolute;top:52px;font-size:15px;color:#3d4148;text-decoration:none;line-height:20px}
.nav a.active{color:var(--ink)}
.nav .underline{position:absolute;left:401px;top:79px;width:51px;height:2px;background:var(--red)}
.header-phone{left:969px;top:52px;font-size:15px;color:var(--red);line-height:20px}

/* Hero */
.hero{left:0;top:110px;width:1200px;height:498px;background:var(--hero-bg)}
.hero-photo{left:760px;top:110px;width:440px;height:498px;background:radial-gradient(circle at 60% 55%,#f4f7fb 0%,#dfe8f2 45%,#c8dcee 75%,#a9cde9 100%)}
.hero-title{left:144px;top:212px;width:640px;font-size:32px;font-weight:600;line-height:41px;color:var(--ink)}
.hero-title em{font-style:normal;color:var(--red)}
.hero-text{left:144px;top:362px;width:540px;font-size:12.5px;line-height:16px;letter-spacing:.3px;color:var(--muted)}
.btn{display:flex;align-items:center;justify-content:center;background:var(--red);color:var(--white);font-weight:600;border-radius:2px}
.hero-btn{left:144px;top:442px;width:174px;height:42px;font-size:15px}

/* About */
.about{left:0;top:608px;width:1200px;height:511px;background:linear-gradient(180deg,#ffffff 0%,#f4f7fb 100%)}
.section-title{font-size:31px;font-weight:600;color:var(--ink);line-height:40px}
.about-title{left:144px;top:725px}
.bar{height:5px;background:var(--red);border-radius:3px;width:68px}
.about-bar{left:144px;top:780px}
.about-text{left:144px;top:805px;width:395px;font-size:12.3px;line-height:15.8px;color:#2f2f2f}
.about-text p+p{margin-top:15.8px}
.about-accent{left:663px;top:702px;width:481px;height:360px;background:var(--red)}
.about-photo{left:637px;top:666px;width:480px;height:361px;background:linear-gradient(180deg,#6b93c6 0%,#8fb0d6 38%,#6d7a86 52%,#8a9a55 72%,#4a4d52 100%)}

/* Services */
.services-bar{left:566px;top:1149px}
.services-title{left:0;top:1160px;width:1200px;text-align:center}
.services-intro{left:300px;top:1213px;width:600px;text-align:center;font-size:12.3px;line-height:16.8px;color:var(--muted)}
.card{top:1334px;width:184px;height:226px;background:var(--white);box-shadow:0 2px 10px var(--card-shadow);text-align:center}
.card svg{position:absolute;left:66px;top:22px}
.card h3{position:absolute;left:0;width:100%;font-size:15.5px;font-weight:700;color:#1f1f1f;line-height:20px}
.card p{position:absolute;left:14px;width:156px;font-size:12px;line-height:16.8px;color:#333}

/* Brochure */
.brochure-art{left:187px;top:1681px;width:343px;height:274px;background:linear-gradient(160deg,#ef4d52 0%,#ec1f27 45%,#f2f2f2 55%,#e4e4e4 100%);clip-path:polygon(0 35%,70% 0,100% 62%,30% 100%)}
.brochure-title{left:666px;top:1694px}
.brochure-text{left:666px;top:1767px;width:350px;font-size:12.4px;line-height:16.6px;color:#2f2f2f}
.download-btn{left:666px;top:1876px;width:177px;height:43px;font-size:20px;letter-spacing:.5px}

/* Footer */
.site-footer{left:0;top:2025px;width:1200px;height:213px;background:var(--red-deep)}
.footer-brand{left:170px;top:2070px;font-size:19px;font-weight:700;letter-spacing:2px;color:var(--white);line-height:1}
.footer-nav a{position:absolute;top:2068px;font-size:15px;color:var(--white);text-decoration:none;line-height:20px}
.footer-nav i{position:absolute;top:2098px;height:1px;background:rgba(255,255,255,.8)}
.footer-contact{left:494px;top:2147px;font-size:15px;color:var(--white);line-height:20px}
.footer-phone{left:607px;top:2146px;display:flex;align-items:center;gap:9px;font-size:15px;font-weight:600;color:var(--white);line-height:20px}
.copyright{left:0;top:2208px;width:1200px;text-align:center;font-size:11.5px;font-weight:600;color:var(--white)}
</style>
</head>
<body>
<div class="page">

  <header class="site-header abs">
  </header>
  <div class="brand abs">ORBAN QUILL</div>
  <nav class="nav">
    <a class="active" style="left:403px">Home</a>
    <a style="left:492px">QPPV</a>
    <a style="left:577px">Our Services</a>
    <a style="left:722px">Contact Us</a>
    <a style="left:846px">Client</a>
    <span class="underline"></span>
  </nav>
  <div class="header-phone abs">0330 555 0142</div>

  <section class="hero abs"></section>
  <div class="hero-photo abs" role="img" aria-label="Stethoscope with a light blue tube on a pale background"></div>
  <h1 class="hero-title abs">At Orban Quill we ensure that your business has the <em>best Pharmacovigilance support</em> in the industry</h1>
  <p class="hero-text abs">We are an outsourcing partner to large and small companies within the pharmaceutical industry. Our range of services is tailored to suit each of our client’s needs and cover both human and veterinary medicinal products.</p>
  <div class="btn hero-btn abs">How we can help</div>

  <section class="about abs"></section>
  <h2 class="section-title about-title abs">About us</h2>
  <div class="bar about-bar abs"></div>
  <div class="about-text abs">
    <p>We are an outsourcing partner to large and small companies within the pharmaceutical industry.Our range of services is tailored to suit each of our client’s needs and cover both human and veterinary medicinal products.</p>
    <p>Pharmacovigilance is defined by WHO as ‘The science and activities relating to the detection, assessment, understanding and prevention of adverse effects or any other drug-related problems’.</p>
  </div>
  <div class="about-accent abs"></div>
  <div class="about-photo abs" role="img" aria-label="Modern glass office building with trees and a road in front under a blue sky"></div>

  <div class="bar services-bar abs"></div>
  <h2 class="section-title services-title abs">Our servises</h2>
  <p class="services-intro abs">Our primary functions are EU QPPV and related pharmacovigilance services to assist and support Marketing Authorisation Holders (MAH), of pharmaceutical product licences, in their efforts to remain compliant with EU regulatory requirements (Regulation 1235/2010 and Directive 2010/84/EU) the deadline for which implementing ended on 21 July 2012</p>

  <div class="card abs" style="left:145px">
    <svg width="52" height="54" viewBox="0 0 52 54" fill="none" stroke="#ec1f27" stroke-width="3" stroke-linecap="round" stroke-linejoin="round">
      <rect x="5" y="2" width="42" height="49" rx="6"/>
      <path d="M26 10v12M20.8 13l10.4 6M31.2 13l-10.4 6"/>
      <path d="M15 31h22M15 38h22"/>
    </svg>
    <h3 style="top:94px">Medical Information</h3>
    <p style="top:122px">Professional enquiry handling to support the safe and effective use of your products</p>
  </div>

  <div class="card abs" style="left:387px">
    <svg width="52" height="54" viewBox="0 0 52 54" fill="none" stroke="#ec1f27" stroke-width="3.5" stroke-linecap="round" stroke-linejoin="round">
      <path d="M1 29h12l6-14 10 26 6-12h16"/>
    </svg>
    <h3 style="top:94px">Pharmacovigilance</h3>
    <p style="top:122px">Ease the regulatory burden and keep compliant with current pharmacovigilance legislation</p>
  </div>

  <div class="card abs" style="left:628px">
    <svg width="52" height="54" viewBox="0 0 52 54" fill="none" stroke="#ec1f27" stroke-width="2.8" stroke-linecap="round" stroke-linejoin="round">
      <path d="M24 46H9V6h24l6 6v16"/>
      <path d="M15 15h12M15 22h16M15 29h9"/>
      <circle cx="33" cy="38" r="6"/>
      <path d="M37.5 42.5l5 5"/>
    </svg>
    <h3 style="top:90px">Literature<br>Monitoring</h3>
    <p style="top:138px">Product safety through surveillance of published articles and case reports</p>
  </div>

  <div class="card abs" style="left:870px">
    <svg width="52" height="54" viewBox="0 0 52 54" fill="none" stroke="#ec1f27" stroke-width="3" stroke-linecap="round" stroke-linejoin="round">
      <circle cx="16" cy="18" r="7"/>
      <circle cx="34" cy="18" r="7"/>
      <path d="M3 43c0-8 6-13 13-13s13 5 13 13z"/>
      <path d="M24 32c3-2 6-2 10-2 7 0 13 5 13 13H29"/>
    </svg>
    <h3 style="top:94px">Training</h3>
    <p style="top:122px">Confident staff to support the pharmacovigilance process</p>
  </div>

  <div class="brochure-art abs" role="img" aria-label="Stack of red and white pharmacovigilance support brochures"></div>
  <h2 class="section-title brochure-title abs">Download our brochure</h2>
  <p class="brochure-text abs">Lorem ipsum dolor sit amet, consectetur adipiscing elit. Duis non ante urna. In vulputate tortor at tellus sagittis iaculis. Fusce pulvinar tellus et mi lobortis mattis. Nam tempor in metus vitae feugiat. Ut nec maximus turpis, at dapibus elit. I</p>
  <div class="btn download-btn abs">Download</div>

  <footer class="site-footer abs"></footer>
  <div class="footer-brand abs">ORBAN QUILL</div>
  <nav class="footer-nav">
    <a style="left:447px">About us</a><i style="left:450px;width:60px"></i>
    <a style="left:583px">QPPV</a><i style="left:572px;width:60px"></i>
    <a style="left:691px">Our services</a><i style="left:703px;width:60px"></i>
    <a style="left:852px">METS</a><i style="left:842px;width:60px"></i>
  </nav>
  <div class="footer-contact abs">Contact us</div>
  <div class="footer-phone abs">
    <svg width="16" height="16" viewBox="0 0 24 24" fill="none" stroke="#ffffff" stroke-width="2" stroke-linejoin="round"><path d="M5 3h4l2 5-3 2a12 12 0 0 0 6 6l2-3 5 2v4a2 2 0 0 1-2 2A18 18 0 0 1 3 5a2 2 0 0 1 2-2z"/></svg>
    <span>0330 555 0142</span>
  </div>
  <div class="copyright abs">Copyright © 2020 Orban Quill Ltd (Registered in England &amp; Wales : 08214670)</div>

</div>
</body>
</html>
```